i need a Marquee Daily blog design

hi, i need a blog which have Marquee Daily news. My blog should be attractive and mature with a good theme. Readers of my blog should be able to comment. You can include any attractive colour (blue, green, purple, red).

Target Market(s)

Celebrity fans and enthusiasts

Industry/Entity Type

News

```html
<!DOCTYPE html>
<html lang="en">
<head>
<meta charset="utf-8">
<title>Marquee Daily</title>
<link href="https://fonts.googleapis.com/css2?family=Open+Sans:wght@400;600;700&family=Raleway:wght@400;500&family=Share+Tech+Mono&display=swap" rel="stylesheet">
<style>
:root{
  --teal:#1ab5bf;
  --teal-dark:#12939b;
  --ink:#3a3a3a;
  --muted:#777;
  --orange:#ef7d12;
  --star:#f0a500;
  --band:#ebebeb;
  --panel:#2b2b2b;
  --footer:#323232;
  --rule:#d8d8d8;
  --white:#fff;
}
*{box-sizing:border-box;margin:0;padding:0}
html,body{width:912px;height:1200px;overflow:hidden;background:var(--white)}
body{position:relative;font-family:"Open Sans",sans-serif;color:var(--ink)}
.abs{position:absolute}

/* header */
.site-header{position:absolute;left:0;top:0;width:912px;height:120px;border-bottom:2px solid #c9c9c9}
.brand{left:75px;top:14px;width:165px;height:86px;background:var(--teal);border-bottom:3px solid var(--teal-dark)}
.brand-name{position:absolute;left:0;right:0;top:18px;text-align:center;color:var(--white);font-weight:700;font-size:25px;letter-spacing:.2px;font-family:"Open Sans",sans-serif}
.brand-rule{position:absolute;top:62px;height:1px;width:70px;background:rgba(255,255,255,.8)}
.nav-active{left:384px;top:0;width:53px;height:102px;background:var(--teal);border-bottom:3px solid var(--teal-dark)}
.nav a{position:absolute;top:56px;font-family:"Raleway",sans-serif;font-size:10px;color:#333;text-decoration:none;letter-spacing:-.2px}

/* hero */
.hero-band{left:0;top:120px;width:912px;height:338px;background:var(--band)}
.slide{left:75px;top:139px;width:504px;height:298px;background:linear-gradient(160deg,#5b8fa3 0%,#6a4a3a 45%,#3a2a24 100%)}
.slide-ctrl{top:334px;width:32px;height:31px;background:var(--teal)}
.slide-track{left:169px;top:349px;width:403px;height:1px;background:rgba(255,255,255,.7)}
.caption{left:75px;top:372px;width:439px;height:65px;background:rgba(25,25,25,.88);padding:10px 10px}
.caption h2{font-size:11px;font-weight:400;color:var(--white);letter-spacing:-.1px;margin-bottom:6px}
.caption p{font-size:7.4px;line-height:12px;color:#ccc}
.date-box{left:514px;top:372px;width:65px;height:65px;background:var(--teal);color:var(--white);text-align:center}
.date-box b{display:block;font-size:30px;font-weight:400;line-height:36px;margin-top:8px}
.date-box span{font-size:9px}
.latest{left:594px;top:139px;width:243px;height:298px;background:var(--panel)}
.latest-item{position:absolute;left:16px;width:211px;height:59px}
.latest-item .thumb{position:absolute;left:0;top:16px;width:59px;height:29px}
.latest-item h3{position:absolute;left:74px;top:14px;font-size:7.6px;font-weight:400;line-height:11.5px;color:var(--white)}
.latest-item h3.hot{color:var(--teal)}
.latest-item small{position:absolute;left:74px;top:38px;font-size:6.6px;color:#666}
.latest-item.lined{border-bottom:1px solid #444}

/* section heads */
.sec-head{height:25px;border-bottom:1px solid}
.sec-head span{display:inline-block;height:25px;padding:4px 7px 0;color:var(--white);font-weight:700;font-size:14px}
.sec-head.teal{border-color:var(--teal)} .sec-head.teal span{background:var(--teal)}
.sec-head.grey{border-color:#777} .sec-head.grey span{background:#555}

/* article cards */
.card{width:238px;height:258px;background:var(--white);box-shadow:0 0 4px rgba(0,0,0,.25);padding:6px}
.card .photo{position:relative;width:225px;height:144px}
.rating{position:absolute;right:0;bottom:0;width:52px;height:14px;background:rgba(0,0,0,.75);font-size:6px;line-height:14px;text-align:center;letter-spacing:1px;color:#aaa}
.rating i{font-style:normal;color:var(--star)}
.card h3{margin:12px 0 0 1px;font-size:11.6px;font-weight:400;line-height:15.5px;color:#444}
.card .meta{margin:10px 0 0 1px;font-size:6.8px;color:var(--orange);letter-spacing:-.2px}
.card p{margin:8px 0 0 1px;font-size:7.3px;line-height:12px;color:#555}

/* sidebar */
.gossip{left:612px;width:225px;height:53px;border-bottom:1px solid var(--rule)}
.gossip h4{font-size:7.6px;font-weight:400;color:#333;margin-top:0}
.gossip .meta{font-size:7.6px;color:var(--orange);margin-top:2px}
.stars{font-size:6px;letter-spacing:1px;color:#bbb}
.stars i{font-style:normal;color:var(--star)}
.news{left:612px;width:225px;height:58px}
.news .thumb{position:absolute;left:0;top:0;width:102px;height:56px}
.news .date{position:absolute;left:116px;top:0;font-size:7.4px;color:var(--orange)}
.news h4{position:absolute;left:116px;top:15px;width:112px;font-size:7.4px;font-weight:600;line-height:11.5px;color:#333;text-align:justify}
.news .stars{position:absolute;left:116px;bottom:0}
.news-rule{left:612px;width:225px;height:1px;background:var(--rule)}
.promo{left:612px;top:977px;width:225px;height:93px;background:linear-gradient(90deg,#1d1a1a 0%,#3b2c24 55%,#7a5a44 100%)}
.promo p{position:absolute;left:0;right:0;top:34px;text-align:center;font-family:"Share Tech Mono",monospace;color:var(--white);font-size:14px;letter-spacing:2px;line-height:20px}
.promo p span{color:var(--star);font-size:15px;letter-spacing:0}

/* footer */
.site-footer{left:0;top:1096px;width:912px;height:104px;background:var(--footer);text-align:center;color:var(--white)}
.socials{position:absolute;left:0;right:0;top:17px;display:flex;justify-content:center;gap:9px}
.socials span{width:14px;height:14px;border-radius:50%;background:var(--white)}
.foot-nav{position:absolute;left:0;right:0;top:50px;font-family:"Raleway",sans-serif;font-size:8.4px}
.foot-nav em{font-style:normal;margin:0 5px}
.copyright{position:absolute;left:0;right:0;top:72px;font-family:"Raleway",sans-serif;font-size:8px;letter-spacing:-.2px}
.page-code{position:absolute;right:37px;top:48px;font-size:8px;color:#ddd}
</style>
</head>
<body>

<header class="site-header">
  <div class="abs brand">
    <div class="brand-name">MARQUEE DAILY</div>
    <div class="brand-rule" style="left:8px"></div>
    <div class="brand-rule" style="left:86px"></div>
  </div>
  <div class="abs nav-active"></div>
  <nav class="nav">
    <a style="left:398px;color:#fff">HOME</a>
    <a style="left:445px">BLOG</a>
    <a style="left:489px">ARTICLES</a>
    <a style="left:550px">FEATURES</a>
    <a style="left:615px">POSTS</a>
    <a style="left:664px">GOSSIPS</a>
    <a style="left:722px">INTERVIEWS</a>
    <a style="left:795px">CONTACT</a>
  </nav>
</header>

<section class="abs hero-band"></section>
<div class="abs slide" role="img" aria-label="Featured photo of a smiling singer at a red carpet event"></div>
<div class="abs slide-ctrl" style="left:100px"><svg width="32" height="31"><path d="M18 11l-4 4.5 4 4.5" stroke="#fff" stroke-width="1" fill="none"/></svg></div>
<div class="abs slide-ctrl" style="left:134px"><svg width="32" height="31"><path d="M14 11l4 4.5-4 4.5" stroke="#fff" stroke-width="1" fill="none"/></svg></div>
<div class="abs slide-track"></div>
<div class="abs caption">
  <h2>VOLUPTATEM ACCUSANTIUM DOLOREMQUE LAUDANTIUM, TOTAM REM APERIAM</h2>
  <p>Lorem ipsum dolor sit amet, consectetur adipiscing elit, sed do eiusmod tempor incididunt ut labore et dolore<br>magna aliqua. Ut enim ad minim veniam, quis nostrud exercitation ullamco</p>
</div>
<div class="abs date-box"><b>12</b><span>March</span></div>

<aside class="abs latest">
  <div class="latest-item lined" style="top:0">
    <div class="thumb" role="img" aria-label="Thumbnail of an actress" style="background:linear-gradient(90deg,#8a6a55,#3a2a22)"></div>
    <h3 class="hot">THE NIGHT BEFORE 3: THE TRILOGY<br>FINALE TEASER TRAILER LEAKED</h3>
    <small>15 Comments // 12 March</small>
  </div>
  <div class="latest-item lined" style="top:59px">
    <div class="thumb" role="img" aria-label="Thumbnail of a blonde singer" style="background:linear-gradient(90deg,#8899aa,#d8c9a8)"></div>
    <h3>LENA ROWE AND MARA QUINN TO PERFORM AT<br>HELEN WARD'S 50TH?</h3>
    <small>15 Comments // 12 March</small>
  </div>
  <div class="latest-item lined" style="top:118px">
    <div class="thumb" role="img" aria-label="Thumbnail of an older director" style="background:linear-gradient(90deg,#2a2a2a,#b8a898)"></div>
    <h3>'STEEL WING 3' SECRETS REVEALED:<br>DANIEL HART EXPLAINS IT ALL</h3>
    <small>15 Comments // 12 March</small>
  </div>
  <div class="latest-item lined" style="top:177px">
    <div class="thumb" role="img" aria-label="Thumbnail of an actor in sunglasses" style="background:linear-gradient(90deg,#5a4a40,#a8b8c8)"></div>
    <h3>NORA BLAKE'S IVY LANE VOTED<br>BRITAIN'S FAVOURITE  MOVIE MOM</h3>
    <small>15 Comments // 12 March</small>
  </div>
  <div class="latest-item" style="top:236px">
    <div class="thumb" role="img" aria-label="Thumbnail of an actress with curly hair" style="background:linear-gradient(90deg,#6a4a34,#c89a6a)"></div>
    <h3>NORA BLAKE'S IVY LANE VOTED<br>BRITAIN'S FAVOURITE  MOVIE MOM</h3>
    <small>15 Comments // 12 March</small>
  </div>
</aside>

<div class="abs sec-head teal" style="left:75px;top:499px;width:492px"><span>ARTICLES</span></div>

<article class="abs card" style="left:75px;top:538px">
  <div class="photo" role="img" aria-label="Actress with long dark hair at a premiere" style="background:linear-gradient(90deg,#111 0%,#3a2a22 50%,#6a5040 100%)"><div class="rating"><i>★★★★</i>★</div></div>
  <h3>DENOUNCING PLEASURE AND PRAISING PAIN WAS BORN AND I WILL ...</h3>
  <div class="meta">14 MARCH 2015  // 45 COMMENTS</div>
  <p>Ever since the first 'The Night Before' movie (which also had an equally amazing movie trailer), people across the country have been enamored by the magic of black-out drinking...</p>
</article>
<article class="abs card" style="left:329px;top:538px">
  <div class="photo" role="img" aria-label="Smiling actor in a suit" style="background:linear-gradient(90deg,#2a2a2a 0%,#8a6a55 50%,#1a1a1a 100%)"><div class="rating"><i>★★★★</i>★</div></div>
  <h3>DENOUNCING PLEASURE AND PRAISING PAIN WAS BORN AND I WILL ...</h3>
  <div class="meta">12 MARCH 2015  // 45 COMMENTS</div>
  <p>Ever since the first 'The Night Before' movie (which also had an equally amazing movie trailer), people across the country have been enamored by the magic of black-out drinking...</p>
</article>
<article class="abs card" style="left:75px;top:812px">
  <div class="photo" role="img" aria-label="Singer performing on stage with a microphone" style="background:linear-gradient(135deg,#2a2a5a 0%,#4a2a3a 50%,#1a1a2a 100%)"><div class="rating"><i>★★★★</i>★</div></div>
  <h3>DENOUNCING PLEASURE AND PRAISING PAIN WAS BORN AND I WILL ...</h3>
  <div class="meta">10 MARCH 2015  // 45 COMMENTS</div>
  <p>Ever since the first 'The Night Before' movie (which also had an equally amazing movie trailer), people across the country have been enamored by the magic of black-out drinking...</p>
</article>
<article class="abs card" style="left:329px;top:812px">
  <div class="photo" role="img" aria-label="Smiling actress at a film festival" style="background:linear-gradient(90deg,#2a3a5a 0%,#7a6050 50%,#6a1a1a 100%)"><div class="rating"><i>★★★</i>★★</div></div>
  <h3>DENOUNCING PLEASURE AND PRAISING PAIN WAS BORN AND I WILL ...</h3>
  <div class="meta">12 MARCH 2015  // 45 COMMENTS</div>
  <p>Ever since the first 'The Night Before' movie (which also had an equally amazing movie trailer), people across the country have been enamored by the magic of black-out drinking...</p>
</article>

<div class="abs sec-head grey" style="left:612px;top:498px;width:225px"><span>GOSSIPS</span></div>
<div class="abs gossip" style="top:538px">
  <h4>LOREM IPSUM DOLOR SIT AMET, CONSECTETUR ADIPISCING</h4>
  <div class="meta">11 MARCH 2015 // ENTERTAINMENT // 47 COMMENTS</div>
  <div class="stars"><i>★★★</i>★★</div>
</div>
<div class="abs gossip" style="top:591px">
  <h4>LOREM IPSUM DOLOR SIT AMET, CONSECTETUR ADIPISCING</h4>
  <div class="meta">12 MARCH 2015 // ENTERTAINMENT // 47 COMMENTS</div>
  <div class="stars"><i>★★★</i>★★</div>
</div>
<div class="abs gossip" style="top:643px">
  <h4>LOREM IPSUM DOLOR SIT AMET, CONSECTETUR ADIPISCING</h4>
  <div class="meta">12 MARCH 2015 // ENTERTAINMENT // 47 COMMENTS</div>
  <div class="stars"><i>★★★</i>★★</div>
</div>

<div class="abs sec-head grey" style="left:612px;top:706px;width:225px"><span>NEWS</span></div>
<div class="abs news" style="top:748px">
  <div class="thumb" role="img" aria-label="Actress at a film premiere" style="background:linear-gradient(90deg,#2a3a5a,#7a6050,#6a1a1a)"></div>
  <div class="date">12 MARCH 2015</div>
  <h4>APERIAM, EAQUE IPSA QUAE AB ILLO INVENTORE VERITATIS</h4>
  <div class="stars"><i>★★★</i>★★</div>
</div>
<div class="abs news-rule" style="top:812px"></div>
<div class="abs news" style="top:820px">
  <div class="thumb" role="img" aria-label="Young actor against a teal backdrop" style="background:linear-gradient(90deg,#2a3a4a,#9a7a65,#2ab0c0)"></div>
  <div class="date">13 MARCH 2015</div>
  <h4>APERIAM, EAQUE IPSA QUAE AB ILLO INVENTORE VERITATIS</h4>
  <div class="stars"><i>★★★</i>★★</div>
</div>
<div class="abs news-rule" style="top:884px"></div>
<div class="abs news" style="top:892px">
  <div class="thumb" role="img" aria-label="Singer performing on stage" style="background:linear-gradient(135deg,#2a2a5a,#4a2a3a,#1a1a2a)"></div>
  <div class="date">14 MARCH 2015</div>
  <h4>APERIAM, EAQUE IPSA QUAE AB ILLO INVENTORE VERITATIS</h4>
  <div class="stars"><i>★★★</i>★★</div>
</div>
<div class="abs news-rule" style="top:956px"></div>

<div class="abs promo" role="img" aria-label="Banner with a portrait of a model">
  <p>BEST CELEBRITY IN<br><span>2015</span></p>
</div>

<footer class="abs site-footer">
  <div class="socials"><span></span><span></span><span></span></div>
  <div class="foot-nav">Home<em>/</em>Blog<em>/</em>Articles<em>/</em>Features<em>/</em>Posts<em>/</em>Gossips<em>/</em>Interviews<em>/</em>Contact</div>
  <div class="copyright">Copyrights@marquee daily 2015 Allrights Reserved.</div>
  <div class="page-code">C11</div>
</footer>

</body>
</html>
```